Web design for financial services

A modern web design of financial services (brokerage firm)
Req.s and technology tags :
- Very mobile friendly.
- One paged with some inner pages.
- Animated sticky header .
- Member login area for e-trade.
- Support RTL language.
- HTML & CSS.

The logo will be Home link
• OKDM :
WHO WE ARE
Content :
i) Board of Directors
ii) Mission Statement
iii) Corporate Values
iv) Regulations
• Financial Services :
WHAT WE DO
Content:
i) Electronic trading
ii) Trading desk
iii) Institutional
iv) Investors Education
• News
• Market Tools
• Forms---- opens new page
• Careers---- opens new page
• Contact Us----opens new page

The website is :
http://www.okdm-pelorn.com/

The logo need some changes to be more modern and impressively , but with keeping same structure .

Some related websites :
https://www.vu-markt.com/

Target Market(s)

financial market

Industry/Entity Type

Financial Service

Coding

Coded - Design and coding required

Number of Pages Required

2 page

Other font styles liked:
• same fonts of http://www.ryntholders.com/

Requirements
Must have
• - Very mobile friendly.
• - One paged with some inner pages.
• - Animated sticky header .
• - Member login area for e-trade.
• - Support RTL language.
• - HTML & CSS.
Nice to have
• Slider , some Qatari theme,
• i like the video inside the home page
• ex :http://www.ryntholders.com/

```html
<!DOCTYPE html>
<html lang="en">
<head>
<meta charset="utf-8">
<title>OKDM — Financial Services</title>
<link rel="stylesheet" href="https://fonts.googleapis.com/css2?family=Montserrat:wght@700;800&family=Merriweather+Sans:wght@400;700&display=swap">
<style>
:root{
  --navy:#0c2a55;
  --nav-bg:#e3e7e9;
  --ink:#1c1c1c;
  --text:#333;
  --gold:#f5c518;
  --date:#c4862c;
  --red-brand:#c2272d;
  --light:#f4f4f4;
  --up:#2a9a2a;
  --down:#d42a2a;
}
*{box-sizing:border-box;margin:0;padding:0}
html,body{width:1200px;height:2568px;overflow:hidden}
body{font-family:"Merriweather Sans",Arial,sans-serif;color:var(--text);background:#fff;position:relative}
a{text-decoration:none;color:inherit}

.topbar{height:43px;background:var(--navy);position:relative;font-size:12px;font-weight:700;color:#fff}
.topbar .login{position:absolute;left:905px;top:14px;display:flex;align-items:center;gap:8px}
.topbar .lang{position:absolute;left:1018px;top:14px}

.mainnav{height:73px;background:var(--nav-bg);position:relative}
.brand{position:absolute;left:128px;top:6px;display:flex;align-items:center;gap:12px}
.brand .mark{width:40px;height:40px;background:var(--red-brand)}
.brand .name{font-weight:700;font-size:48px;color:var(--ink);letter-spacing:1px;line-height:60px}
.mainnav ul{list-style:none;position:absolute;top:28px;left:553px;display:flex}
.mainnav li{font-weight:700;font-size:14px;color:var(--navy);margin-right:22px}

.hero{position:absolute;left:7px;top:116px;width:1186px;height:562px;
  background:radial-gradient(ellipse at 50% 40%,#3c4a5a 0%,#1d2530 45%,#0b0f14 100%)}
.hero .photo{position:absolute;inset:0}
.hero h1{position:absolute;top:180px;width:100%;text-align:center;font-family:Montserrat,sans-serif;font-weight:800;font-size:44px;color:#fff;letter-spacing:-1.5px}
.hero p{position:absolute;top:252px;width:100%;text-align:center;font-weight:700;font-size:18px;line-height:26px;color:#fff}
.hero .cta{position:absolute;left:488px;top:316px;width:162px;height:34px;background:var(--navy);color:#fff;font-size:13px;font-weight:700;display:flex;align-items:center;justify-content:center;gap:8px}

.about{position:absolute;top:678px;left:0;width:1200px;height:443px}
.section-title{font-weight:700;font-size:30px;color:var(--ink)}
.about .section-title{position:absolute;left:125px;top:52px}
.about .lead{position:absolute;left:125px;top:112px;width:440px;font-size:16.5px;font-weight:400;line-height:27px;color:var(--ink)}
.about .body{position:absolute;left:125px;top:183px;width:455px;font-size:11.6px;line-height:22.8px;color:var(--text)}
.about .photo{position:absolute;left:613px;top:120px;width:462px;height:277px;background:linear-gradient(135deg,#cfd6d8,#8d9a99 55%,#5d6461)}

.services{position:absolute;top:1121px;left:7px;width:1186px;height:379px;
  background:linear-gradient(90deg,#0b2440 0%,#1a4f78 45%,#12456d 70%,#0a2848 100%)}
.services .section-title{position:absolute;top:45px;width:100%;text-align:center;color:#fff}
.service-card{position:absolute;top:122px;width:306px;height:202px;background:rgba(246,247,249,.96);text-align:center;padding:26px 20px 0}
.service-card h3{font-size:16px;font-weight:700;color:var(--navy);margin-bottom:12px}
.service-card p{font-size:12.4px;line-height:19.5px;color:#2b2b2b;white-space:nowrap}
.service-card .more{display:inline-flex;align-items:center;gap:6px;margin-top:16px;font-size:11px;font-weight:700;color:var(--ink)}

.news{position:absolute;top:1500px;left:0;width:1200px;height:486px;background:var(--light)}
.news .section-title{position:absolute;top:60px;width:100%;text-align:center}
.news-card{position:absolute;top:135px;width:230px;height:269px;background:#fff;border:2px solid #d6d6d6}
.news-card .thumb{height:161px}
.news-card h3{font-size:13.6px;line-height:22px;font-weight:700;color:var(--navy);margin:16px 0 0 19px;width:195px}
.news-card time{display:flex;align-items:center;gap:8px;margin:14px 0 0 19px;font-size:11.5px;font-weight:400;color:var(--date)}

.partners{position:absolute;top:1986px;left:0;width:1200px;height:125px}
.partner{position:absolute;top:46px;display:flex;align-items:center;gap:8px;font-size:22px;color:#444}
.partner .dot{width:22px;height:22px}

.markets{position:absolute;top:2111px;left:7px;width:1186px;height:401px;
  background:radial-gradient(ellipse at 50% 30%,#34404e 0%,#1b232c 55%,#0a0d12 100%)}
.markets .section-title{position:absolute;top:47px;width:100%;text-align:center;color:#fff}
.market-card{position:absolute;top:123px;width:306px;height:226px;background:#ececec;padding:20px 0 0}
.market-card h3{text-align:center;font-size:16px;font-weight:700;color:var(--navy);margin-bottom:10px}
.market-card table{margin:0 auto;border-collapse:collapse;font-family:Arial,sans-serif;font-size:9.6px;color:#222}
.market-card th{font-weight:700;padding:0 9px 2px;text-align:left;border-bottom:1px solid #999}
.market-card td{padding:0 9px;line-height:12px}
.market-card td:nth-child(2){text-align:right}
.up{color:var(--up)}.down{color:var(--down)}

.footer{position:absolute;top:2512px;left:0;width:1200px;height:56px;background:var(--navy);color:#c9d3e0;font-size:11px;padding:20px 0 0 112px}
</style>
</head>
<body>

<header>
  <div class="topbar">
    <a class="login" href="#">
      <svg width="12" height="14" viewBox="0 0 12 14"><rect x="1" y="6" width="10" height="8" rx="1" fill="var(--gold)"/><path d="M3 6V4a3 3 0 0 1 6 0v2" stroke="var(--gold)" stroke-width="1.8" fill="none"/></svg>
      Login
    </a>
    <a class="lang" href="#">English</a>
  </div>
  <nav class="mainnav">
    <a class="brand" href="#"><span class="mark"></span><span class="name">OKDM</span></a>
    <ul>
      <li>OKDM</li>
      <li>Financial Services</li>
      <li>News</li>
      <li>Market Tools</li>
      <li>Forms</li>
      <li>Contact Us</li>
    </ul>
  </nav>
</header>

<section class="hero">
  <div class="photo" role="img" aria-label="Business team reviewing financial charts on a dark meeting table"></div>
  <h1>Lorem Ipsum Aliquyam</h1>
  <p>Duis autem vel eum iriure dolor in hendrerit<br>in vulputate velit esse molestie consequat.</p>
  <a class="cta" href="#">Our Financial Services
    <svg width="7" height="10" viewBox="0 0 7 10"><path d="M1 1l4 4-4 4" stroke="#fff" stroke-width="2" fill="none"/></svg>
  </a>
</section>

<section class="about">
  <h2 class="section-title">Who We Are</h2>
  <p class="lead">Lorem ipsum dolor sit amet consetetur sadipscing elitr sed diam nonumy eirmod tempor invidunt.</p>
  <p class="body">Lorem ipsum dolor sit amet consetetur sadipscing elitr velit sed diam nonumy eirmod tempor invidunt ut labore et dolore magna aliquyam erat sed diam voluptua. Stet clita kasd gubergren no sea takimata sanctus est Lorem ipsum dolor sit amet hendrerit in vulputate no sea takimata sanctus est Lorem ipsum dolor sit amet hendrerit in vulputate. At vero eos et accusam et justo duo dolores et ea rebum. Stet clita kasd gubergren no sea takimata sanctus est Lorem ipsum dolor sit amet. Lorem ipsum dolor sit amet consetetur sadipscing elitr sed diam nonumy eirmod tempor invidunt ut labore et dolore magna aliquyam erat sed diam voluptua at vero eos et.</p>
  <div class="photo" role="img" aria-label="Colleagues meeting around a conference table in a bright office"></div>
</section>

<section class="services" aria-label="What We Do">
  <h2 class="section-title">What We Do</h2>
  <article class="service-card" style="left:106px">
    <h3>Takimata Sanctus</h3>
    <p>Lorem ipsum dolor sit amet setetur<br>sadipscing elitr sed diam nonumy<br>eirmod tempor invidunt ut labore<br>bunet dolore magna aliquyam erat.</p>
    <a class="more" href="#">read more <svg width="6" height="9" viewBox="0 0 6 9"><path d="M1 1l3 3.5L1 8" stroke="#222" stroke-width="1.8" fill="none"/></svg></a>
  </article>
  <article class="service-card" style="left:440px">
    <h3>Euismod Tincidunt</h3>
    <p>Lorem ipsum dolor sit amet setetur<br>sadipscing elitr sed diam nonumy<br>eirmod tempor invidunt ut labore<br>bunet dolore magna aliquyam erat.</p>
    <a class="more" href="#">read more <svg width="6" height="9" viewBox="0 0 6 9"><path d="M1 1l3 3.5L1 8" stroke="#222" stroke-width="1.8" fill="none"/></svg></a>
  </article>
  <article class="service-card" style="left:774px">
    <h3>Praesent Luptatum</h3>
    <p>Lorem ipsum dolor sit amet setetur<br>sadipscing elitr sed diam nonumy<br>eirmod tempor invidunt ut labore<br>bunet dolore magna aliquyam erat.</p>
    <a class="more" href="#">read more <svg width="6" height="9" viewBox="0 0 6 9"><path d="M1 1l3 3.5L1 8" stroke="#222" stroke-width="1.8" fill="none"/></svg></a>
  </article>
</section>

<section class="news">
  <h2 class="section-title">News</h2>
  <article class="news-card" style="left:99px">
    <div class="thumb" role="img" aria-label="Shopper thinking in a supermarket aisle" style="background:linear-gradient(135deg,#c98a7a,#7c5a6a 50%,#c9a94a)"></div>
    <h3>Utwisi Enim Adminim Veniam Strud Exercitation</h3>
    <time><svg width="11" height="11" viewBox="0 0 11 11"><circle cx="5.5" cy="5.5" r="4.6" stroke="#333" stroke-width="1.2" fill="none"/><path d="M5.5 3v2.7h2" stroke="#333" stroke-width="1.2" fill="none"/></svg>February 1, 2017</time>
  </article>
  <article class="news-card" style="left:356px">
    <div class="thumb" role="img" aria-label="Trader watching market screens" style="background:linear-gradient(135deg,#3d4a5e,#1c2530 60%,#6b4030)"></div>
    <h3>Duis Autem veleum Iriure Dolor Hendrerit Vulputate</h3>
    <time><svg width="11" height="11" viewBox="0 0 11 11"><circle cx="5.5" cy="5.5" r="4.6" stroke="#333" stroke-width="1.2" fill="none"/><path d="M5.5 3v2.7h2" stroke="#333" stroke-width="1.2" fill="none"/></svg>February 1, 2017</time>
  </article>
  <article class="news-card" style="left:613px">
    <div class="thumb" role="img" aria-label="Chess pieces on a board" style="background:linear-gradient(135deg,#6a6660,#3a3632 55%,#9a928a)"></div>
    <h3>Invidunt Labore Dolore Magna Aliquyam Voluptua</h3>
    <time><svg width="11" height="11" viewBox="0 0 11 11"><circle cx="5.5" cy="5.5" r="4.6" stroke="#333" stroke-width="1.2" fill="none"/><path d="M5.5 3v2.7h2" stroke="#333" stroke-width="1.2" fill="none"/></svg>February 1, 2017</time>
  </article>
  <article class="news-card" style="left:871px">
    <div class="thumb" role="img" aria-label="Shopper thinking in a supermarket aisle" style="background:linear-gradient(135deg,#c98a7a,#7c5a6a 50%,#c9a94a)"></div>
    <h3>Vel Illum Dolore Feugiat Nulla Facilisis Takimata</h3>
    <time><svg width="11" height="11" viewBox="0 0 11 11"><circle cx="5.5" cy="5.5" r="4.6" stroke="#333" stroke-width="1.2" fill="none"/><path d="M5.5 3v2.7h2" stroke="#333" stroke-width="1.2" fill="none"/></svg>January 29, 2017</time>
  </article>
</section>

<section class="partners" aria-label="Partners">
  <div class="partner" style="left:135px"><span class="dot" style="background:#f26b2a"></span>Rovel</div>
  <div class="partner" style="left:282px"><span class="dot" style="background:#e63946"></span>Vellora</div>
  <div class="partner" style="left:465px"><span class="dot" style="background:#f3b51b;border-radius:50%"></span>Brisko</div>
  <div class="partner" style="left:622px"><span class="dot" style="background:#2fb8a6"></span>Quenta</div>
  <div class="partner" style="left:828px"><span class="dot" style="background:#e8452a"></span>Lumo</div>
  <div class="partner" style="left:990px"><span class="dot" style="background:#222;border-radius:50%"></span>Dorvani</div>
</section>

<section class="markets" aria-label="Market Tools">
  <h2 class="section-title">Market Tools</h2>
  <article class="market-card" style="left:106px">
    <h3>Most Active Company</h3>
    <table>
      <tr><th>Company</th><th>Last</th><th>Change</th></tr>
      <tr><td>PLVA</td><td>15.01</td><td class="down">-0.82%</td></tr>
      <tr><td>TRNO</td><td>8.45</td><td class="up">+0.11%</td></tr>
      <tr><td>KESL</td><td>40.60</td><td class="up">+1.24%</td></tr>
      <tr><td>DUVO</td><td>34.30</td><td class="down">-0.58%</td></tr>
      <tr><td>FENR</td><td>24.05</td><td class="down">-0.62%</td></tr>
      <tr><td>HALM</td><td>31.00</td><td class="down">-0.47%</td></tr>
      <tr><td>JORV</td><td>164.00</td><td class="up">+1.11%</td></tr>
      <tr><td>LUMT</td><td>36.60</td><td class="up">+0.83%</td></tr>
      <tr><td>NEXR</td><td>22.35</td><td class="down">-0.82%</td></tr>
      <tr><td>ORBY</td><td>9.75</td><td class="up">+0.52%</td></tr>
    </table>
  </article>
  <article class="market-card" style="left:440px">
    <h3>Top Gainers</h3>
    <table>
      <tr><th>Company</th><th>Last</th><th>Change</th></tr>
      <tr><td>PESK</td><td>54.00</td><td class="up">+4.31%</td></tr>
      <tr><td>KESL</td><td>40.60</td><td class="up">+1.24%</td></tr>
      <tr><td>JORV</td><td>164.00</td><td class="up">+1.11%</td></tr>
      <tr><td>LUMT</td><td>36.60</td><td class="up">+0.83%</td></tr>
      <tr><td>RAVO</td><td>91.40</td><td class="up">+0.77%</td></tr>
      <tr><td>SOLT</td><td>11.69</td><td class="up">+0.60%</td></tr>
      <tr><td>ORBY</td><td>9.75</td><td class="up">+0.52%</td></tr>
      <tr><td>TAVN</td><td>68.00</td><td class="up">+0.29%</td></tr>
      <tr><td>UVRA</td><td>15.80</td><td class="up">+0.26%</td></tr>
      <tr><td>WEMB</td><td>14.41</td><td class="up">+0.21%</td></tr>
    </table>
  </article>
  <article class="market-card" style="left:774px">
    <h3>Top Losers</h3>
    <table>
      <tr><th>Company</th><th>Last</th><th>Change</th></tr>
      <tr><td>XELO</td><td>36.00</td><td class="down">-4.00%</td></tr>
      <tr><td>YARN</td><td>14.00</td><td class="down">-1.95%</td></tr>
      <tr><td>ZEPH</td><td>64.00</td><td class="down">-1.82%</td></tr>
      <tr><td>BRIV</td><td>222.00</td><td class="down">-1.77%</td></tr>
      <tr><td>CALN</td><td>103.00</td><td class="down">-1.72%</td></tr>
      <tr><td>DRAV</td><td>63.20</td><td class="down">-1.54%</td></tr>
      <tr><td>ELKO</td><td>50.00</td><td class="down">-1.38%</td></tr>
      <tr><td>FIRN</td><td>16.51</td><td class="down">-1.30%</td></tr>
      <tr><td>GLYP</td><td>84.00</td><td class="down">-1.18%</td></tr>
      <tr><td>HESK</td><td>20.20</td><td class="down">-0.98%</td></tr>
    </table>
  </article>
</section>

<footer class="footer">Copyright © 2017 OKDM. All Rights Reserved.</footer>

</body>
</html>
```